Postcard Design

We provide humorous speechwriting and presentation coaching services, primarily for the wedding market (best man, father of the bride, maid of honor). We'd like a design that incoporates the blue and white logo colors into a nice overall design, with the pitch:
"Use the power of humor to deliver the BEST speech of your life!"
Target Market(s)
Wedding market (best man, bride/groom)
Industry/Entity Type
Wedding
Requirements
Must have
- Bulletpoints for services provided:
- Speechwriting
- Presentation Coaching
- Emcee & Officiant Services
Listing of benefits provided:
- Conquer stage fright
- Deliver your speech like a pro
- Be funny AND tactful
- Leave them wanting more
Contact info -
Trent Halvorsen
Trent@QuipCraftly.com
www.QuipCraftly.com
Testimonial quotes:
"People are STILL raving about that speech at our wedding. Thanks Quip Craftly!"
- Dana & Paul Fenwick, Baltimore, MD
"With the help of Quip Craftly, my best man speech brought down the house!"
- Mark Delahunt, Melville, NY

```html
<!DOCTYPE html>
<html lang="en">
<head>
<meta charset="utf-8">
<title>Quip Craftly — Postcard</title>
<link href="https://fonts.googleapis.com/css2?family=Mouse+Memoirs&display=swap" rel="stylesheet">
<style>
  :root {
    --mint: #b6ded6;
    --mint-light: #e6f5f0;
    --navy: #27275e;
    --badge-navy: #1b2b5e;
    --service-blue: #1565b8;
    --white: #ffffff;
    --cake-pink: #dfa3a8;
    --cake-pink-light: #eebcc0;
    --podium-wood: #b87a3c;
  }
  * { margin: 0; padding: 0; box-sizing: border-box; }
  html, body { width: 1200px; height: 929px; overflow: hidden; }
  body { font-family: "Mouse Memoirs", "Arial Narrow", sans-serif; }

  .postcard {
    position: relative;
    width: 1200px;
    height: 929px;
    overflow: hidden;
    background: radial-gradient(ellipse 620px 520px at 900px 300px, var(--mint-light) 0%, var(--mint) 70%);
  }

  .headline {
    position: absolute;
    left: 66px;
    top: 52px;
    font-size: 90px;
    line-height: 92px;
    font-weight: 400;
    color: var(--navy);
    letter-spacing: 0.5px;
  }

  .services {
    position: absolute;
    left: 66px;
    top: 380px;
    list-style: none;
  }
  .services li {
    display: flex;
    align-items: center;
    gap: 10px;
    height: 48px;
    font-size: 42px;
    color: var(--service-blue);
  }
  .services svg { width: 26px; height: 26px; flex: none; }

  .brand-badge {
    position: absolute;
    left: 64px;
    top: 592px;
    width: 276px;
    height: 276px;
    border-radius: 50%;
    background: var(--badge-navy);
    display: flex;
    align-items: center;
    justify-content: center;
    text-align: center;
    color: var(--white);
    font-size: 52px;
    line-height: 48px;
    letter-spacing: 1px;
  }

  .cake-podium-art {
    position: absolute;
    left: 520px;
    top: 226px;
    width: 680px;
    height: 703px;
    border-radius: 340px 340px 0 0 / 120px 120px 0 0;
    background: linear-gradient(180deg, var(--podium-wood) 0%, var(--cake-pink-light) 36%, var(--cake-pink) 100%);
  }
</style>
</head>
<body>
  <main class="postcard">
    <h1 class="headline">Use the power of humor<br>to deliver the BEST speech<br>of your life!</h1>

    <ul class="services">
      <li>
        <svg viewBox="0 0 26 26" aria-hidden="true"><rect x="2" y="4" width="20" height="20" rx="3" fill="none" stroke="#ffffff" stroke-width="2.5"/><path d="M7 13 l5 5 L24 4" fill="none" stroke="#ffffff" stroke-width="3" stroke-linecap="round" stroke-linejoin="round"/></svg>
        Speechwriting
      </li>
      <li>
        <svg viewBox="0 0 26 26" aria-hidden="true"><rect x="2" y="4" width="20" height="20" rx="3" fill="none" stroke="#ffffff" stroke-width="2.5"/><path d="M7 13 l5 5 L24 4" fill="none" stroke="#ffffff" stroke-width="3" stroke-linecap="round" stroke-linejoin="round"/></svg>
        Presentation Coaching
      </li>
      <li>
        <svg viewBox="0 0 26 26" aria-hidden="true"><rect x="2" y="4" width="20" height="20" rx="3" fill="none" stroke="#ffffff" stroke-width="2.5"/><path d="M7 13 l5 5 L24 4" fill="none" stroke="#ffffff" stroke-width="3" stroke-linecap="round" stroke-linejoin="round"/></svg>
        Emcee &amp; Officiant Services
      </li>
    </ul>

    <div class="brand-badge">QUIP<br>CRAFTLY</div>

    <div class="cake-podium-art" role="img" aria-label="Illustration of a wooden podium with two microphones standing on top of a three-tier pink wedding cake with white dotted trim"></div>
  </main>
</body>
</html>
```